Brasko Construction Business Card

I need a business card design for my company.
We are a construction/machinery company.
I would like to see my logo on the front of the card and my details on the other side
I would like the card to be black or dark grey in colour,with my logo as i send it or modified with a lighter blue colour
I would like to see the design kept fairly simple,but eye catching at the same time
Industry/Entity Type
Business
Contact Information for Business Card
Name
Phone Number
Address
Email
Colors
00a990
1b1b1b
000000
474747
ececec

```html
<!DOCTYPE html>
<html lang="en">
<head>
<meta charset="utf-8">
<title>Brasko Construction Business Card</title>
<link href="https://fonts.googleapis.com/css2?family=Roboto:wght@400;700;900&family=Oswald:wght@600&display=swap" rel="stylesheet">
<style>
  :root {
    --stage: #2f2724;
    --card: #3a3a3c;
    --card-edge: #2a2a2b;
    --teal: #52c2a4;
    --text-light: #ececec;
    --text-muted: #c9c9c9;
  }
  * { margin: 0; padding: 0; box-sizing: border-box; }
  html, body {
    width: 1200px;
    height: 716px;
    overflow: hidden;
    background: var(--stage);
    font-family: "Roboto", Arial, sans-serif;
  }
  .stage {
    width: 1200px;
    height: 716px;
    display: flex;
    align-items: center;
    justify-content: center;
    gap: 50px;
  }
  .card {
    width: 525px;
    height: 300px;
    background: var(--card);
    border-radius: 3px;
    box-shadow: 0 2px 0 var(--card-edge);
    position: relative;
  }
  .card-front {
    display: flex;
    align-items: center;
    justify-content: center;
  }
  .wordmark {
    display: flex;
    align-items: center;
    gap: 12px;
    color: var(--teal);
    font-weight: 900;
    text-transform: uppercase;
    line-height: 1;
  }
  .wordmark-square {
    width: 44px;
    height: 44px;
    background: var(--teal);
    flex: none;
  }
  .wordmark-name {
    display: flex;
    flex-direction: column;
    gap: 4px;
  }
  .wordmark-name .primary { font-size: 40px; letter-spacing: 1px; }
  .wordmark-name .secondary { font-size: 17px; letter-spacing: 3.5px; }

  .card-back { padding: 0 36px 0 38px; display: flex; align-items: center; justify-content: space-between; }
  .card-back .wordmark-square { width: 32px; height: 32px; }
  .card-back .wordmark-name .primary { font-size: 30px; }
  .card-back .wordmark-name .secondary { font-size: 12.5px; letter-spacing: 2.8px; }

  .contact { width: 220px; color: var(--text-light); }
  .contact-name {
    font-family: "Oswald", "Arial Narrow", sans-serif;
    font-weight: 600;
    color: var(--teal);
    font-size: 19px;
    line-height: 1.1;
  }
  .contact-role { font-size: 11px; color: var(--text-muted); margin-bottom: 12px; }
  .contact-list { list-style: none; font-size: 13px; line-height: 1.45; }
  .contact-list li { display: flex; align-items: center; gap: 9px; }
  .contact-list svg { width: 10px; height: 10px; flex: none; fill: var(--teal); }
  .contact-address { font-size: 13px; line-height: 1.4; margin-top: 2px; }
</style>
</head>
<body>
<main class="stage">
  <section class="card card-front" aria-label="Card front">
    <div class="wordmark">
      <span class="wordmark-square"></span>
      <span class="wordmark-name">
        <span class="primary">Brasko</span>
        <span class="secondary">Construction</span>
      </span>
    </div>
  </section>

  <section class="card card-back" aria-label="Card back">
    <div class="wordmark">
      <span class="wordmark-square"></span>
      <span class="wordmark-name">
        <span class="primary">Brasko</span>
        <span class="secondary">Construction</span>
      </span>
    </div>
    <div class="contact">
      <p class="contact-name">Your Good Name</p>
      <p class="contact-role">General Contractor</p>
      <ul class="contact-list">
        <li>
          <svg viewBox="0 0 10 10" aria-hidden="true"><path d="M2 0.5 L3.6 2.8 L2.7 3.8 Q3.6 5.9 6.2 7.3 L7.2 6.4 L9.5 8 L8.3 9.5 Q4.5 9.5 1.8 6.4 Q0.3 4.3 0.6 1.7 Z"/></svg>
          <span>+00 111 222 3333</span>
        </li>
        <li>
          <svg viewBox="0 0 10 10" aria-hidden="true"><path d="M0 2 H10 V8.5 H0 Z M0.6 2.4 L5 5.6 L9.4 2.4 V2.2 H0.6 Z" fill-rule="evenodd"/></svg>
          <span>www.yourwebsite.com</span>
        </li>
        <li>
          <svg viewBox="0 0 10 10" aria-hidden="true"><circle cx="5" cy="5" r="4.5" fill="none" stroke="#52c2a4" stroke-width="1.2"/><circle cx="5" cy="5" r="1.8"/></svg>
          <span>yourname@yourwebsite.com</span>
        </li>
      </ul>
      <p class="contact-address">Your Long Commercial or<br>business address in 2 line</p>
    </div>
  </section>
</main>
</body>
</html>
```